Redesign our company's business card. HSG BUSINESS CARD 2015

We are an Audio Visual Production company with a flare of marketing and sales. Lights camera ACTION!! We are Production and creative designers and thinkers whom provide first class service for many vantage 300 companies that Exhibit at trade shows and sales meetings.

Double sided, sleek, fashionable, and modern.

www.halvernstudio.com

Think ZNQ'S Crestline

Target Market(s)

Trade Show Mangers, Event coordinators, Project managers,

Industry/Entity Type

Marketing

Contact Information for Business Card

Name Tile, Logo, Slogan, photos of our work on the back. Chatterly and blipper

Font styles to use
Sans Serif
Decorative
Script

Colors
33a6d7
ffffff
0692cd
cee9f5

Requirements
Must have
• Multi color, professional, Upscale,
• CREATING GREAT PARTNERSHIPS THAT PRODUCE AMAZING RESULTS
Nice to have
• Photos of our work on the back
Should not have
• Address or fax.

```html
<!DOCTYPE html>
<html lang="en">
<head>
<meta charset="utf-8">
<title>HSG Business Card</title>
<link href="https://fonts.googleapis.com/css2?family=Play:wght@400;700&display=swap" rel="stylesheet">
<style>
  :root{
    --page:#e9ecef;
    --card:#ffffff;
    --blue-deep:#1c63b8;
    --blue-bright:#3a90dc;
    --silver:#a9b1b8;
    --silver-dark:#7f8890;
    --name-blue:#1f5fa8;
    --title-grey:#3c3f44;
    --on-blue:#ffffff;
  }
  html,body{margin:0;padding:0;width:1200px;height:900px;overflow:hidden;background:var(--page);}
  .business-card{
    position:absolute;left:100px;top:165px;width:1000px;height:570px;
    background:var(--card);border-radius:46px;overflow:hidden;
    box-shadow:0 14px 40px rgba(0,0,0,.18);
    font-family:"Play",sans-serif;
  }
  .card-art{position:absolute;inset:0;}
  .brand{position:absolute;left:60px;top:100px;display:flex;align-items:center;gap:26px;color:var(--silver-dark);}
  .brand-dot{width:110px;height:110px;border-radius:50%;background:var(--blue-bright);}
  .brand-name{font-size:78px;font-weight:700;letter-spacing:6px;line-height:1;}
  .brand-full{font-size:17px;font-weight:700;letter-spacing:3px;text-transform:uppercase;margin-top:6px;}
  .person{position:absolute;left:48px;top:300px;}
  .person-name{font-size:34px;font-weight:700;color:var(--name-blue);letter-spacing:2px;line-height:1.2;}
  .person-title{font-size:22px;font-weight:700;color:var(--title-grey);letter-spacing:2px;margin-top:2px;}
  .slogan{position:absolute;left:48px;top:500px;color:var(--on-blue);font-size:17px;line-height:1.5;letter-spacing:1px;font-weight:700;}
  .contacts{position:absolute;right:44px;top:190px;color:var(--on-blue);font-size:19px;letter-spacing:1px;
    display:flex;flex-direction:column;align-items:flex-end;gap:8px;}
  .contact-line{display:flex;align-items:center;gap:10px;}
  .contact-line svg{width:18px;height:18px;fill:none;stroke:var(--on-blue);stroke-width:2;}
</style>
</head>
<body>
<div class="business-card">
  <svg class="card-art" viewBox="0 0 1000 570" preserveAspectRatio="none">
    <defs>
      <linearGradient id="blueSweep" x1="0" y1="1" x2="1" y2="0">
        <stop offset="0" stop-color="var(--blue-deep)"/>
        <stop offset="1" stop-color="var(--blue-bright)"/>
      </linearGradient>
    </defs>
    <path class="silver-arc" d="M0,456 C340,436 592,280 622,0 L644,0 C598,285 340,452 0,468 Z" fill="var(--silver)"/>
    <path class="blue-field" d="M655,0 L1000,0 L1000,570 L0,570 L0,480 C340,460 600,290 655,0 Z" fill="url(#blueSweep)"/>
  </svg>

  <div class="brand">
    <div class="brand-dot"></div>
    <div>
      <div class="brand-name">HSG</div>
      <div class="brand-full">Halvern Studio Group</div>
    </div>
  </div>

  <div class="person">
    <div class="person-name">DANA REYES</div>
    <div class="person-title">PRESIDENT</div>
  </div>

  <div class="slogan">CREATING GREAT PARTNERSHIPS<br>THAT PRODUCE AMAZING RESULTS</div>

  <div class="contacts">
    <div class="contact-line">014 552 7310
      <svg viewBox="0 0 24 24"><path d="M5 3h4l2 5-3 2a12 12 0 0 0 6 6l2-3 5 2v4a2 2 0 0 1-2 2A18 18 0 0 1 3 5a2 2 0 0 1 2-2z"/></svg></div>
    <div class="contact-line">014 552 7311
      <svg viewBox="0 0 24 24"><rect x="7" y="2" width="10" height="20" rx="2"/><line x1="11" y1="18" x2="13" y2="18"/></svg></div>
    <div class="contact-line">hello@halvernstudio.com
      <svg viewBox="0 0 24 24"><rect x="3" y="5" width="18" height="14" rx="1"/><path d="M3 6l9 7 9-7"/></svg></div>
    <div class="contact-line">www.halvernstudio.com
      <svg viewBox="0 0 24 24"><circle cx="12" cy="12" r="9"/><path d="M3 12h18M12 3c3 3 3 15 0 18M12 3c-3 3-3 15 0 18"/></svg></div>
  </div>
</div>
</body>
</html>
```